Lakeshore Freightways Council Web Update

Update wordpress based association web site. Please look up www.lakeshorefreightwayscouncil.com for our web site to get a feel for what we currently having. We would like our updated web site to look similar to: www.brightoakfund.com. We will provide our key points for updating in a future email.

Target Market(s)

duplicate the brightoakfund.com format please.

Number of Pages Required

4 page

Font styles to use
Serif

Requirements
Must have
• duplicate the brightoakfund.com format please. You will keep most of the content that we currently have on our website.
Nice to have
• n/a
Should not have
• n/a

```html
<!DOCTYPE html>
<html lang="en">
<head>
<meta charset="utf-8">
<title>Lakeshore Freightways Council</title>
<link href="https://fonts.googleapis.com/css2?family=Mulish:ital,wght@0,400;0,600;0,700;1,400&display=swap" rel="stylesheet">
<style>
:root{
  --navy:#2a2275;
  --navy-band:#231d85;
  --navy-deep:#0e0b4d;
  --rose:#b5545a;
  --red-btn:#b8454d;
  --ink:#1c1c1c;
  --charcoal:#161616;
  --white:#ffffff;
  --grey-line:#c9c9c9;
  --field:#f1f1f1;
  --hero-tone-a:#6b6668;
  --hero-tone-b:#7d5e5c;
  --gravel-a:#8a8178;
  --gravel-b:#766b60;
  --field-green-a:#6f8260;
  --field-green-b:#626a58;
}
*{margin:0;padding:0;box-sizing:border-box}
html,body{width:1200px;height:2970px;overflow:hidden;background:var(--white)}
body{font-family:"Mulish",Arial,sans-serif;color:var(--ink);position:relative}
.abs{position:absolute}
h1,h2{font-weight:400}

/* header */
.site-header{left:0;top:0;width:1200px;height:100px;background:var(--white);z-index:3}
.brand{left:112px;top:0;width:160px;height:138px;background:var(--white);
  clip-path:polygon(0 0,100% 0,100% 88%,92% 100%,8% 100%,0 88%);
  display:flex;align-items:center;justify-content:center;text-align:center;
  color:var(--navy);font-weight:700;font-size:17px;line-height:1.25;text-transform:uppercase;letter-spacing:1px;padding:0 14px;z-index:4}
.main-nav{right:174px;top:40px;display:flex;gap:35px;font-size:14px;letter-spacing:.5px;color:#7a7a7a}
.main-nav .active{color:var(--navy);font-weight:700}

/* hero */
.hero{left:0;top:100px;width:1200px;height:525px;
  background:linear-gradient(180deg,var(--hero-tone-a),var(--hero-tone-b))}
.hero-title{left:123px;top:280px;color:var(--white);font-size:37px;font-weight:700;line-height:1.2;letter-spacing:.5px}
.hero-sub{left:120px;top:382px;color:var(--white);font-size:19px;line-height:1.2;width:420px}
.hero-dots{left:552px;top:587px;display:flex;gap:9px}
.hero-dots span{width:14px;height:14px;border-radius:50%;background:var(--white)}
.hero-dots span:first-child{background:transparent;border:2px solid var(--white)}

.welcome{left:0;top:665px;width:1200px;text-align:center;font-size:34px}

/* feature blocks */
.photo{display:block}
.panel{color:var(--white)}
.panel h2{font-size:28px;letter-spacing:1px;margin-bottom:24px}
.panel p{font-size:13.5px;line-height:2}
.btn-outline{display:inline-block;border:2px solid var(--white);color:var(--white);font-size:15px;padding:9px 30px;margin-top:24px;letter-spacing:.5px}

.what-photo{left:0;top:745px;width:600px;height:438px;background:linear-gradient(180deg,#7a7468,#6c6a66)}
.what-panel{left:600px;top:745px;width:528px;height:438px;background:var(--navy);padding:66px 60px 0 62px}
.what-strip{left:1128px;top:745px;width:72px;height:438px;background:linear-gradient(180deg,var(--gravel-a),var(--gravel-b))}

.who-strip{left:0;top:1183px;width:97px;height:437px;background:linear-gradient(180deg,var(--gravel-a),var(--gravel-b))}
.who-panel{left:97px;top:1183px;width:503px;height:437px;background:var(--rose);padding:72px 56px 0 56px}
.who-photo{left:600px;top:1183px;width:600px;height:437px;background:linear-gradient(180deg,var(--gravel-a),var(--gravel-b))}

/* quote */
.leader-avatar{left:155px;top:1727px;width:134px;height:134px;border-radius:50%;background:#8a8e95}
.leader-name{left:140px;top:1876px;width:164px;text-align:center;font-size:14px;letter-spacing:.5px}
.leader-role{left:140px;top:1897px;width:164px;text-align:center;font-size:14px;color:var(--rose);letter-spacing:.5px}
.quote-rule{left:307px;top:1728px;width:1px;height:150px;background:var(--grey-line)}
.quote{left:360px;top:1742px;width:705px;font-size:13px;font-style:italic;line-height:25px;color:#333}
.quote-mark{color:var(--rose);font-size:38px;font-weight:700;line-height:1;font-style:normal}
.q-open{left:324px;top:1730px}
.q-close{display:inline-block;vertical-align:-14px;margin-left:6px;height:25px}

/* join */
.join-photo{left:0;top:1968px;width:612px;height:447px;background:linear-gradient(180deg,var(--field-green-a),var(--field-green-b))}
.join-panel{left:612px;top:1968px;width:516px;height:447px;background:var(--charcoal);padding:96px 60px 0 74px}
.join-strip{left:1128px;top:1968px;width:72px;height:447px;background:linear-gradient(180deg,var(--field-green-a),var(--field-green-b))}

/* newsletter */
.news-title{left:0;top:2477px;width:1200px;text-align:center;font-size:27px;letter-spacing:.5px}
.field{top:2547px;height:43px;border:1px solid #bdbdbd;background:var(--field);font-size:14px;color:#777;padding:12px 18px}
.f-name{left:155px;width:328px}
.f-mail{left:495px;width:330px}
.btn-subscribe{left:838px;top:2547px;width:185px;height:43px;background:var(--red-btn);color:var(--white);font-size:15px;font-weight:600;display:flex;align-items:center;justify-content:center;letter-spacing:.5px}

/* contact band */
.contact-band{left:0;top:2680px;width:1200px;height:128px;background:var(--navy-band);color:var(--white)}
.contact-item{top:30px;font-size:15px;line-height:1.4}
.contact-item svg{display:block;margin-bottom:6px}
.contact-item .big{font-size:18px}

/* footer */
.site-footer{left:0;top:2808px;width:1200px;height:162px;background:var(--navy-deep);color:var(--white)}
.foot-nav{left:123px;top:52px;display:flex;gap:34px;font-size:13px}
.copyright{left:123px;top:84px;font-size:11.5px;color:#a9a7c9}
.badge{left:763px;top:22px;width:90px;height:114px;background:var(--white)}
.social{top:47px;display:flex;gap:8px;left:914px}
.social span{width:36px;height:36px;border-radius:50%;border:2px solid var(--white)}
</style>
</head>
<body>

<header class="site-header abs">
  <div class="brand abs">Lakeshore Freightways Council</div>
  <nav class="main-nav abs">
    <span class="active">HOME</span><span>WHAT WE DO</span><span>WHO WE ARE</span><span>WHO WE SERVE</span><span>RESOURCES</span>
  </nav>
</header>

<section class="hero abs" role="img" aria-label="Freight locomotive pulling a train along the tracks"></section>
<h1 class="hero-title abs">RAILROAD COMPANY<br>INVESTMENTS</h1>
<p class="hero-sub abs">along with education, safety-enhancing technologies and training</p>
<div class="hero-dots abs"><span></span><span></span><span></span><span></span></div>

<h2 class="welcome abs">Welcome to Our Website</h2>

<div class="what-photo photo abs" role="img" aria-label="Rail worker in high-visibility vest working on the track"></div>
<section class="what-panel panel abs">
  <h2>WHAT WE DO</h2>
  <p>The LFC reviews all introduced legislation in the House and Senate. Proposed legislation affecting the rail industry is shared with our members. Final industry positions regarding legislation are then communicated to the legislature.<br>We pursue the same activity with appropriate personnel in the state departments and the legislative rules process.</p>
  <span class="btn-outline">READ MORE</span>
</section>
<div class="what-strip photo abs" role="img" aria-label="Gravel rail bed"></div>

<div class="who-strip photo abs" role="img" aria-label="Rail track detail"></div>
<section class="who-panel panel abs">
  <h2>WHO WE ARE</h2>
  <p>The Lakeshore Freightways Council (LFC) is a non-profit trade association that represents the interests of freight railroads operating in the Lakeshore region. LFC members range in size from large Class 1 interstate carriers to smaller regional carriers and shortline railroads. LFC members account for over 95% of all freight rail moved in the region.</p>
  <span class="btn-outline">READ MORE</span>
</section>
<div class="who-photo photo abs" role="img" aria-label="Railway tracks crossing at a switch"></div>

<div class="leader-avatar abs" role="img" aria-label="Portrait of the council president"></div>
<div class="leader-name abs">DALE RENNER</div>
<div class="leader-role abs">PRESIDENT</div>
<div class="quote-rule abs"></div>
<span class="quote-mark q-open abs">&ldquo;</span>
<p class="quote abs">I would like to welcome you to the Lakeshore Freightways Council website. Here you will find valuable information on regional railroads, including issues and concerns in and around the railroad industry. We are an active and aggressive state railroad association and we look forward to continued success with our partnerships. Please make sure to click on our member railroad company links while you're here. Also, sign up for our newsletter and follow the LFC on Chirpline. Thank you and I hope you enjoy your visit to our website.<span class="quote-mark q-close">&rdquo;</span></p>

<div class="join-photo photo abs" role="img" aria-label="Passenger train passing through countryside"></div>
<section class="join-panel panel abs">
  <h2>HOW TO JOIN LFC</h2>
  <p>LFC membership is open to any freight railroad with regional operations. Please contact the LFC office for membership information. Companies which supply goods or services to the railroad industry are eligible for a non-voting Associate Membership. Annual dues are $1,000 per year for supplier members.</p>
  <span class="btn-outline">READ MORE</span>
</section>
<div class="join-strip photo abs" role="img" aria-label="Trees beside the line"></div>

<h2 class="news-title abs">NEWSLETTER SIGN UP</h2>
<div class="field f-name abs">Your Name</div>
<div class="field f-mail abs">Email address</div>
<div class="btn-subscribe abs">SUBSCRIBE</div>

<section class="contact-band abs">
  <div class="contact-item abs" style="left:123px">
    <svg width="18" height="24" viewBox="0 0 18 24"><path d="M9 0C4 0 0 4 0 9c0 7 9 15 9 15s9-8 9-15c0-5-4-9-9-9zm0 13a4 4 0 110-8 4 4 0 010 8z" fill="#fff"/></svg>
    48 Harbor Row, Suite 310<br>Port Alden, LK 40217
  </div>
  <div class="contact-item abs" style="left:380px">
    <svg width="22" height="22" viewBox="0 0 24 24"><path d="M6.6 10.8a15 15 0 006.6 6.6l2.2-2.2c.3-.3.7-.4 1-.2 1.1.4 2.3.6 3.6.6.6 0 1 .4 1 1V20c0 .6-.4 1-1 1C10.6 21 3 13.4 3 4c0-.6.4-1 1-1h3.5c.6 0 1 .4 1 1 0 1.3.2 2.5.6 3.6.1.3 0 .7-.2 1z" fill="#fff"/></svg>
    <span class="big">(555) 214-0388</span>
  </div>
  <div class="contact-item abs" style="left:578px">
    <svg width="22" height="24" viewBox="0 0 22 24"><rect x="1" y="6" width="20" height="17" rx="2" fill="#fff"/><rect x="5" y="1" width="12" height="7" fill="#fff"/><rect x="5" y="11" width="12" height="3" fill="#231d85"/><rect x="5" y="16" width="3" height="3" fill="#231d85"/><rect x="10" y="16" width="3" height="3" fill="#231d85"/><rect x="15" y="16" width="3" height="3" fill="#231d85"/></svg>
    <span class="big">(555) 214-0391</span>
  </div>
  <div class="contact-item abs" style="left:777px">
    <svg width="22" height="17" viewBox="0 0 22 17"><rect width="22" height="17" rx="1" fill="#fff"/><path d="M1 1l10 8 10-8" stroke="#231d85" stroke-width="2" fill="none"/></svg>
    <span class="big">info@lakeshorefreightwayscouncil.com</span>
  </div>
</section>

<footer class="site-footer abs">
  <nav class="foot-nav abs"><span>HOME</span><span>WHAT WE DO</span><span>WHO WE ARE</span><span>WHO WE SERVE</span><span>RESOURCES</span></nav>
  <p class="copyright abs">© 2017 Company Name &nbsp;All right reserved &nbsp;Term of Use</p>
  <div class="badge abs"></div>
  <div class="social abs"><span></span><span></span><span></span><span></span></div>
</footer>

</body>
</html>
```